Quenly - Property Management Company Listings - PSD / uncoded only

Our site simply connects property owners with property managers. I’m asking you to create 2 pages, 1 homepage and 1 page that lists of property management companies. Build with Responsive Design in mind. PSD/uncoded files only. Help us create a great site!
Example competitor sites:
http://www.everyestatehelpers.example/
http://www.tendyourlots.example/
Inspired by these sites:
http://www.gravlet.example/
http://www.hornbrisk.example/
http://www.coinvex.example/
https://www.lanehive.example/
I've attached the logo as well as 2 picture files that you can consider using.
• Quenly Logo Colors: Yellow: HTML code: #FBC30A, RGB code: R: 251 G: 195 B: 10 Grey: HTML code: #4E4C4D, RGB code: R: 78 G: 76 B: 77
• The picture files are optional.
o One picture is of houses and neighborhood.
o The other is of a professional woman on the phone. Please do not use the professional woman as a large primary image. You can use the professional woman photo as a smaller photo and not the main photo.
• Please bring your own pictures and graphics too. Don't feel like you need to use mine.
Thank you!
Industry/Entity Type
Property Management

```html
<!DOCTYPE html>
<html lang="en">
<head>
<meta charset="utf-8">
<title>Quenly — Property Management Solutions</title>
<link rel="stylesheet" href="https://fonts.googleapis.com/css2?family=Lato:wght@400;700;900&family=Open+Sans:ital,wght@0,400;0,600;0,700;1,400&display=swap">
<style>
  :root {
    --yellow: #fbc30a;
    --grey: #4e4c4d;
    --ink: #333333;
    --topbar: #3b3b3b;
    --blue: #4a86c0;
    --panel: rgba(24, 24, 24, 0.82);
    --footer: #1f1f1f;
    --white: #ffffff;
    --muted: #666666;
  }
  * { box-sizing: border-box; margin: 0; padding: 0; }
  html, body { width: 740px; height: 1200px; overflow: hidden; background: var(--white); }
  body { font-family: "Open Sans", Arial, sans-serif; color: var(--ink); position: relative; }

  /* top bar */
  .topbar { position: absolute; top: 0; left: 0; width: 740px; height: 16px; background: var(--topbar); }
  .topbar__call { position: absolute; left: 484px; top: 2px; font-size: 8px; color: #ddd; display: flex; align-items: center; gap: 4px; }
  .topbar__call b { color: var(--yellow); font-weight: 700; }
  .topbar__login { position: absolute; left: 605px; top: 0; width: 48px; height: 16px; background: var(--blue); color: var(--white); font-size: 7.5px; font-weight: 700; display: flex; align-items: center; justify-content: center; gap: 3px; }

  /* header */
  .header { position: absolute; top: 16px; left: 0; width: 740px; height: 54px; background: var(--white); }
  .brand { position: absolute; left: 88px; top: 14px; display: flex; align-items: center; gap: 6px; }
  .brand__mark { width: 14px; height: 14px; background: var(--yellow); }
  .brand__name { font-family: "Lato", sans-serif; font-weight: 900; font-size: 26px; color: var(--grey); line-height: 1; }
  .nav { position: absolute; left: 410px; top: 24px; display: flex; gap: 22px; font-size: 8.5px; color: var(--ink); }
  .nav__item { position: relative; }
  .nav__item--active { font-weight: 600; }
  .nav__item--active::after { content: ""; position: absolute; left: 0; right: 0; top: 15px; height: 2px; background: var(--yellow); }

  /* hero */
  .hero { position: absolute; top: 70px; left: 0; width: 740px; height: 348px; background: linear-gradient(160deg, #7f8a74 0%, #8b8d8f 35%, #6f7468 65%, #8a8e84 100%); }
  .hero__title { position: absolute; left: 86px; top: 30px; font-family: "Lato", sans-serif; font-weight: 700; font-size: 22px; line-height: 30px; color: var(--white); letter-spacing: 0.2px; }
  .hero__title em { font-style: normal; color: var(--yellow); }
  .hero__arrow { position: absolute; left: 352px; top: 64px; }
  .search { position: absolute; left: 87px; top: 168px; width: 566px; height: 112px; background: var(--panel); border-top: 3px solid var(--yellow); }
  .search__tab { position: absolute; left: 0; top: -17px; width: 56px; height: 14px; background: var(--panel); border-top: 3px solid var(--yellow); }
  .search__title { position: absolute; left: 18px; top: 10px; font-family: "Lato", sans-serif; font-weight: 700; font-size: 16.5px; color: var(--white); }
  .search__desc { position: absolute; left: 18px; top: 33px; font-size: 8.8px; color: #e6e6e6; }
  .search__rule { position: absolute; left: 0; right: 0; top: 53px; border-top: 1px dashed rgba(255,255,255,0.18); }
  .search__select { position: absolute; left: 16px; top: 66px; width: 297px; height: 29px; background: var(--white); font-size: 8px; color: var(--ink); padding-left: 9px; display: flex; align-items: center; }
  .search__select-btn { position: absolute; right: 5px; top: 4px; width: 20px; height: 20px; border-radius: 50%; background: var(--blue); display: flex; align-items: center; justify-content: center; }
  .search__zip { position: absolute; left: 327px; top: 66px; width: 125px; height: 29px; background: var(--white); font-size: 8px; color: var(--muted); padding-left: 9px; display: flex; align-items: center; }
  .search__btn { position: absolute; left: 464px; top: 66px; width: 86px; height: 29px; background: var(--blue); color: var(--white); font-size: 10.5px; font-weight: 600; display: flex; align-items: center; justify-content: center; }
  .hero__pointer { position: absolute; left: 355px; top: 418px; width: 0; height: 0; border-left: 15px solid transparent; border-right: 15px solid transparent; border-top: 15px solid #6f7468; }

  /* steps */
  .steps__title { position: absolute; top: 442px; left: 0; width: 740px; text-align: center; font-size: 15.5px; font-weight: 600; color: var(--ink); }
  .step { position: absolute; top: 485px; width: 160px; text-align: center; font-size: 9.5px; line-height: 14px; color: #444; }
  .step svg { display: block; margin: 0 auto 7px; }
  .step--one { left: 96px; }
  .step--two { left: 289px; }
  .step--three { left: 483px; }
  .steps__arrow { position: absolute; top: 516px; }

  /* features band */
  .features { position: absolute; top: 620px; left: 0; width: 740px; height: 162px; background: linear-gradient(180deg, #64708a 0%, #55606a 45%, #3f5a37 100%); }
  .feature { position: absolute; top: 33px; width: 200px; text-align: center; color: var(--white); font-size: 10px; line-height: 17px; font-weight: 600; text-shadow: 0 1px 2px rgba(0,0,0,0.5); }
  .feature__icon { width: 58px; height: 58px; border-radius: 50%; background: var(--yellow); margin: 0 auto 10px; display: flex; align-items: center; justify-content: center; }
  .feature--one { left: 68px; }
  .feature--two { left: 269px; }
  .feature--three { left: 469px; }

  /* manager call-out */
  .manager { position: absolute; top: 782px; left: 0; width: 740px; height: 162px; background: linear-gradient(120deg, #dcdcdc 0%, #f4f4f4 45%, #e4e4e4 100%); }
  .manager__photo { position: absolute; left: 100px; top: 8px; width: 140px; height: 154px; border-radius: 60px 60px 0 0; background: linear-gradient(180deg, #c9a88f 0%, #2b2b2e 45%, #1d1d20 100%); }
  .manager__title { position: absolute; left: 270px; top: 32px; font-size: 16px; font-weight: 600; color: var(--ink); }
  .manager__text { position: absolute; left: 270px; top: 58px; width: 388px; font-size: 10.3px; line-height: 18px; color: #444; }
  .manager__btn { position: absolute; left: 270px; top: 105px; width: 87px; height: 25px; background: var(--blue); color: var(--white); font-size: 9px; font-weight: 600; display: flex; align-items: center; justify-content: center; border-radius: 2px; }

  /* review */
  .review__title { position: absolute; top: 964px; left: 0; width: 750px; text-align: center; font-size: 15px; font-weight: 600; }
  .review__sub { position: absolute; top: 987px; left: 0; width: 750px; text-align: center; font-size: 8.5px; color: var(--muted); }
  .review__stars { position: absolute; top: 1001px; left: 359px; display: flex; gap: 1px; }
  .review__rule { position: absolute; top: 1008px; height: 1px; width: 80px; background: #ddd; }
  .review__quote { position: absolute; top: 1027px; left: 87px; width: 490px; height: 60px; background: #efefef; padding: 7px 12px 0 10px; font-size: 8.1px; line-height: 13px; font-style: italic; color: #444; text-indent: 14px; }
  .review__quote::before { content: "\201C"; position: absolute; left: 9px; top: 3px; font-size: 24px; line-height: 1; color: #bbb; font-style: normal; font-family: Georgia, serif; text-indent: 0; }
  .review__quote::after { content: ""; position: absolute; right: -12px; top: 22px; border-top: 8px solid transparent; border-bottom: 8px solid transparent; border-left: 12px solid #efefef; }
  .review__avatar { position: absolute; left: 579px; top: 1020px; width: 75px; height: 75px; border-radius: 50%; border: 3px solid #e5e5e5; background: linear-gradient(180deg, #d9dde2 0%, #9aa6b4 100%); }
  .review__name { position: absolute; top: 1098px; left: 487px; font-size: 7.5px; font-style: italic; font-weight: 600; color: var(--ink); }

  /* footer */
  .footer { position: absolute; top: 1130px; left: 0; width: 740px; height: 70px; background: linear-gradient(180deg, #2c2c2c, var(--footer)); border-top: 2px solid var(--yellow); color: #e5e5e5; font-size: 7.5px; text-align: center; }
  .footer__row { position: absolute; left: 0; width: 740px; display: flex; justify-content: center; gap: 8px; }
  .footer__row span.sep { color: #888; }
  .footer__row--one { top: 12px; }
  .footer__row--two { top: 30px; }
  .footer__copy { position: absolute; top: 48px; left: 0; width: 740px; }
</style>
</head>
<body>

<div class="topbar">
  <div class="topbar__call">
    <svg width="9" height="9" viewBox="0 0 10 10"><circle cx="5" cy="5" r="5" fill="#ddd"/><path d="M3.3 2.6 4.3 3.6 3.8 4.3Q4.6 5.6 5.7 6.2L6.4 5.7 7.4 6.7 6.8 7.4Q4 6.6 2.6 3.2Z" fill="#3b3b3b"/></svg>
    <span><b>Call us :</b> (123) 555-0147</span>
  </div>
  <div class="topbar__login">
    <svg width="7" height="7" viewBox="0 0 10 10"><circle cx="5" cy="3" r="2.4" fill="#fff"/><path d="M0.5 10Q1 5.8 5 5.8T9.5 10Z" fill="#fff"/></svg>
    Login
  </div>
</div>

<header class="header">
  <div class="brand"><span class="brand__mark"></span><span class="brand__name">Quenly</span></div>
  <nav class="nav">
    <span class="nav__item nav__item--active">Home</span>
    <span class="nav__item">Are you a Property Manager?</span>
    <span class="nav__item">Contact Us</span>
  </nav>
</header>

<section class="hero">
  <div role="img" aria-label="Aerial photo of a suburban neighbourhood with houses and trees" style="position:absolute;inset:0;"></div>
  <h1 class="hero__title">PROPERTY MANAGEMENT<br>SOLUTIONS, <em>SIMPLIFIED.</em></h1>
  <svg class="hero__arrow" width="30" height="42" viewBox="0 0 30 42"><path d="M4 4Q24 6 22 34" fill="none" stroke="#fbc30a" stroke-width="2"/><path d="M16 29 22 36 27 28" fill="none" stroke="#fbc30a" stroke-width="2"/></svg>
  <div class="search">
    <div class="search__tab"></div>
    <h2 class="search__title">FIND YOUR LOCAL PROPERTY MANAGER</h2>
    <p class="search__desc">Search our directory to find experienced and professional property management companies that meet your needs.</p>
    <div class="search__rule"></div>
    <div class="search__select">Select Your Property Type
      <span class="search__select-btn"><svg width="10" height="6" viewBox="0 0 10 6"><path d="M1 1 5 5 9 1" fill="none" stroke="#fff" stroke-width="1.8"/></svg></span>
    </div>
    <div class="search__zip">Zipcode</div>
    <div class="search__btn">SEARCH</div>
  </div>
</section>
<div class="hero__pointer"></div>

<h2 class="steps__title">To Find Property Management Companies Near You:</h2>

<div class="step step--one">
  <svg width="76" height="76" viewBox="0 0 76 76"><path d="M4 38A34 34 0 0 1 72 38" fill="none" stroke="#fbc30a" stroke-width="6"/><path d="M72 38A34 34 0 0 1 4 38" fill="none" stroke="#4e4c4d" stroke-width="6"/>
    <path d="M22 38 36 26 50 38" fill="none" stroke="#4e4c4d" stroke-width="3"/><rect x="26" y="37" width="20" height="14" fill="#4e4c4d"/><rect x="30" y="40" width="5" height="5" fill="#fff"/><circle cx="48" cy="48" r="7" fill="#fbc30a"/><path d="M45 48 47.5 50.5 51.5 45.5" fill="none" stroke="#fff" stroke-width="1.8"/></svg>
  Select your property<br>type and zipcode
</div>
<svg class="steps__arrow" style="left:253px" width="40" height="12" viewBox="0 0 40 12"><rect x="0" y="4" width="30" height="4" fill="#b5b5b5"/><path d="M28 0 40 6 28 12Z" fill="#b5b5b5"/></svg>
<div class="step step--two">
  <svg width="76" height="76" viewBox="0 0 76 76"><path d="M4 38A34 34 0 0 1 72 38" fill="none" stroke="#fbc30a" stroke-width="6"/><path d="M72 38A34 34 0 0 1 4 38" fill="none" stroke="#4e4c4d" stroke-width="6"/>
    <circle cx="36" cy="30" r="8" fill="#4e4c4d"/><path d="M22 54Q23 40 36 40T50 54Z" fill="#4e4c4d"/><path d="M42 50 52 38 55 41 45 53 41 54Z" fill="#fbc30a"/></svg>
  Review property manager<br>listings in your area
</div>
<svg class="steps__arrow" style="left:447px" width="40" height="12" viewBox="0 0 40 12"><rect x="0" y="4" width="30" height="4" fill="#b5b5b5"/><path d="M28 0 40 6 28 12Z" fill="#b5b5b5"/></svg>
<div class="step step--three">
  <svg width="76" height="76" viewBox="0 0 76 76"><path d="M4 38A34 34 0 0 1 72 38" fill="none" stroke="#fbc30a" stroke-width="6"/><path d="M72 38A34 34 0 0 1 4 38" fill="none" stroke="#4e4c4d" stroke-width="6"/>
    <circle cx="35" cy="30" r="8" fill="#4e4c4d"/><path d="M21 54Q22 40 35 40T49 54Z" fill="#4e4c4d"/><path d="M43 46 47 50 55 40" fill="none" stroke="#fbc30a" stroke-width="3"/></svg>
  Select and compare<br>property managers
</div>

<section class="features">
  <div role="img" aria-label="Photo of brick family houses along a residential street" style="position:absolute;inset:0;"></div>
  <div class="feature feature--one">
    <div class="feature__icon"><svg width="28" height="24" viewBox="0 0 28 24"><rect x="2" y="16" width="4" height="7" fill="#333"/><rect x="8" y="12" width="4" height="11" fill="#333"/><rect x="14" y="14" width="4" height="9" fill="#333"/><rect x="20" y="9" width="4" height="14" fill="#333"/><path d="M2 12 10 6 15 9 24 2" fill="none" stroke="#333" stroke-width="2"/><path d="M19 1 26 0 25 7Z" fill="#333"/></svg></div>
    Making renting your home an<br>easy, stress-free experience.
  </div>
  <div class="feature feature--two">
    <div class="feature__icon"><svg width="30" height="22" viewBox="0 0 30 22"><circle cx="11" cy="6" r="5" fill="#333"/><path d="M1 21Q2 12 11 12T21 21Z" fill="#333"/><circle cx="20" cy="5" r="4.5" fill="#333"/><path d="M16 11Q20 10 24 11T29 20H23Z" fill="#333"/></svg></div>
    Connecting property owners with<br>property managers.
  </div>
  <div class="feature feature--three">
    <div class="feature__icon"><svg width="26" height="26" viewBox="0 0 26 26"><rect x="2" y="11" width="5" height="13" fill="#333"/><path d="M9 12 14 3Q17 3 16 8L15 11H23Q25 12 24 15L21 23Q20 24 18 24H9Z" fill="#333"/></svg></div>
    Providing property management<br>solutions, simplified.
  </div>
</section>

<section class="manager">
  <div class="manager__photo" role="img" aria-label="Smaller photo of a professional woman in a suit talking on the phone"></div>
  <h2 class="manager__title">Are You A Property Manager?</h2>
  <p class="manager__text">Join our real estate property management company network. Let us help you find leads of property owners seeking to rent their homes.</p>
  <div class="manager__btn">LEARN MORE</div>
</section>

<h2 class="review__title">Our Customer Review</h2>
<p class="review__sub">Lorem ipsum dolor sit amet, consectetur Donec a consequat mag&nbsp; Aenean eu velit&nbsp; Aenean sollicitudin</p>
<div class="review__rule" style="left:276px"></div>
<div class="review__rule" style="left:394px"></div>
<div class="review__stars">
  <svg width="8" height="8" viewBox="0 0 10 10"><path d="M5 0 6.2 3.6H10L7 5.9 8.1 9.5 5 7.3 1.9 9.5 3 5.9 0 3.6H3.8Z" fill="#fbc30a"/></svg>
  <svg width="8" height="8" viewBox="0 0 10 10"><path d="M5 0 6.2 3.6H10L7 5.9 8.1 9.5 5 7.3 1.9 9.5 3 5.9 0 3.6H3.8Z" fill="#fbc30a"/></svg>
  <svg width="8" height="8" viewBox="0 0 10 10"><path d="M5 0 6.2 3.6H10L7 5.9 8.1 9.5 5 7.3 1.9 9.5 3 5.9 0 3.6H3.8Z" fill="#fbc30a"/></svg>
</div>
<blockquote class="review__quote">Lorem sum dolor sit amet, consectetuer adipiscing elit, sed diam nonummy nibh euismod tincidunt ut laoreet re agn aliqam erat volutpat wisi enim ad minim veniam, quis nostrud exerci tation ullamcorper suscipit lobortis nisl ut aliquip modo conseuatis autem vel eum iriure dolor in hendrerit in vulputate velit esse molestie consequat, vel illum dolore eu.</blockquote>
<div class="review__avatar" role="img" aria-label="Portrait photo of the reviewing customer"></div>
<p class="review__name">Marel, Tallowpoint , USA</p>

<footer class="footer">
  <div class="footer__row footer__row--one"><span>Home</span><span class="sep">|</span><span>Are you a Property Manager?</span><span class="sep">|</span><span>About Us</span></div>
  <div class="footer__row footer__row--two"><span>Terms of Use</span><span class="sep">&nbsp;|&nbsp;</span><span>Site Map</span><span class="sep">&nbsp;|&nbsp;</span><span>Contact Us</span></div>
  <p class="footer__copy">Copyright © 2014 Quenly. All Rights Reserved .</p>
</footer>

</body>
</html>
```